Halvery Building Group Website

Need a dynamic corporate website that can be built on with time. We want to get our information out to the world and have a place where customers can submit requests for proposals.

Target Market(s)

Custom home owners and buyers. Architects and Real Estate Agents.

Industry/Entity Type

Construction

Number of Pages Required

3 page

Font styles to use
Serif
Sans Serif

Requirements
Must have
• Company logo, about, company contact information, biography, contact, projects,
• Sleek, modern, clean, attractive design.
• Online form customers can use for filling out a request for project proposal.
• Workcircle hyperlink.
• Uses www.halverybuildinggroup.example

```html
<!DOCTYPE html>
<html lang="en">
<head>
<meta charset="utf-8">
<title>Halvery Building Group</title>
<link rel="stylesheet" href="https://fonts.googleapis.com/css2?family=Roboto:wght@300;400;500;700&family=Roboto+Condensed:wght@700&display=swap">
<style>
  :root {
    --brand-blue: #0a4ea3;
    --band-blue: #0d4f9f;
    --band-orange: #f7a21b;
    --accent-orange: #ff8f00;
    --ink-dark: #1c1c1c;
    --white: #ffffff;
    --link-blue: #0b4aa8;
    --hero-warm-dark: #8a7455;
    --hero-warm-mid: #ab8e62;
    --hero-warm-light: #b89c76;
  }
  * { box-sizing: border-box; margin: 0; padding: 0; }
  html, body { width: 1200px; height: 892px; overflow: hidden; }
  body { font-family: "Roboto", sans-serif; background: var(--white); position: relative; }

  .site-header {
    position: absolute; top: 0; left: 0; width: 1200px; height: 85px;
    border-top: 3px solid var(--brand-blue); background: var(--white);
  }
  .brand { position: absolute; left: 98px; top: 24px; display: flex; align-items: center; gap: 10px; }
  .brand-mark { width: 34px; height: 34px; background: var(--brand-blue); }
  .brand-name { font-size: 25px; font-weight: 500; color: var(--brand-blue); letter-spacing: 0.3px; }
  .menu-toggle { position: absolute; right: 100px; top: 33px; display: flex; align-items: center; gap: 8px;
    color: var(--brand-blue); font-weight: 700; font-size: 16px; }

  .hero { position: absolute; top: 85px; left: 0; width: 1200px; height: 504px; }
  .hero-photo { position: absolute; inset: 0;
    background: linear-gradient(160deg, var(--hero-warm-dark) 0%, var(--hero-warm-mid) 50%, var(--hero-warm-light) 75%, #9e8c78 100%); }
  .hero-content { position: absolute; left: 93px; top: 143px; color: var(--white); }
  .hero-title { font-family: "Roboto Condensed", sans-serif; font-weight: 700; font-size: 40px;
    letter-spacing: 0.2px; line-height: 44px; text-shadow: 0 2px 4px rgba(0,0,0,.35); }
  .hero-lead { margin-top: 14px; font-size: 21px; line-height: 34px; }
  .hero-lead a { color: var(--white); font-style: italic; }
  .btn-contact { position: absolute; left: 2px; top: 169px; width: 136px; height: 44px;
    border: 2px solid var(--white); border-radius: 22px;
    background: linear-gradient(180deg, #ffa21a, #ff7e00); color: var(--white);
    font-weight: 500; font-size: 16px; display: flex; align-items: center; justify-content: center; }
  .slider-dots { position: absolute; left: 1155px; top: 205px; list-style: none; }
  .slider-dots li { width: 11px; height: 11px; border: 2px solid var(--white); border-radius: 50%; margin-bottom: 7.5px; }
  .slider-dots li.active { background: var(--accent-orange); }

  .info-band { position: absolute; top: 589px; left: 0; width: 1200px; height: 245px; display: flex; }
  .nav-panel { width: 600px; height: 100%; background: linear-gradient(135deg, #0e55a8, #0a4793); position: relative; }
  .nav-col { position: absolute; top: 38px; color: var(--white); }
  .nav-col h3, .about-panel h3 { font-size: 17px; font-weight: 500; }
  .nav-col ul { list-style: none; margin-top: 14px; }
  .nav-col li { font-size: 13px; height: 28.5px; display: flex; align-items: center; }
  .nav-col li::before { content: "\203A"; font-size: 15px; width: 27px; padding-left: 2px; }
  .about-panel { width: 600px; height: 100%; background: linear-gradient(135deg, #f8a723, #f59a12);
    color: var(--white); padding: 38px 100px 0 70px; }
  .about-panel p { margin-top: 18px; font-size: 12px; font-weight: 300; line-height: 22.3px; text-align: justify; }
  .about-panel p + p { margin-top: 9px; }
  .read-more { float: right; color: var(--link-blue); }

  .site-footer { position: absolute; top: 834px; left: 0; width: 1200px; height: 58px; background: var(--ink-dark);
    color: var(--white); font-size: 12.5px; }
  .copyright { position: absolute; left: 98px; top: 21px; }
  .footer-nav { position: absolute; right: 100px; top: 21px; display: flex; }
  .footer-nav span + span::before { content: "|"; margin: 0 17px; }
</style>
</head>
<body>
  <header class="site-header">
    <div class="brand"><span class="brand-mark"></span><span class="brand-name">Halvery Building Group</span></div>
    <div class="menu-toggle">
      <svg width="19" height="17" viewBox="0 0 19 17"><rect y="0" width="19" height="3" fill="#0a4ea3"/><rect y="7" width="19" height="3" fill="#0a4ea3"/><rect y="14" width="19" height="3" fill="#0a4ea3"/></svg>
      MENU
    </div>
  </header>

  <section class="hero">
    <div class="hero-photo" role="img" aria-label="Photo of a hard hat and work gloves on a concrete ledge above a city"></div>
    <div class="hero-content">
      <h1 class="hero-title">HALVERY BUILDING GROUP</h1>
      <p class="hero-lead">2000 Latin words, combined with a handful<br>1200 5550 1427 &nbsp;/&nbsp; <a href="#">hello@halvery.example</a></p>
      <a class="btn-contact">CONTACT US</a>
    </div>
    <ul class="slider-dots"><li></li><li></li><li class="active"></li><li></li><li></li></ul>
  </section>

  <section class="info-band">
    <div class="nav-panel">
      <div class="nav-col" style="left:98px"><h3>PROJECTS</h3><ul><li>Commercial</li><li>Residential</li><li>Community</li><li>Location Map</li></ul></div>
      <div class="nav-col" style="left:264px"><h3>PROFILE</h3><ul><li>Team</li><li>Process</li><li>Testimonials</li><li>History</li></ul></div>
      <div class="nav-col" style="left:422px"><h3>CONNECT</h3><ul><li>Email</li><li>Chirpline</li><li>Friendwall</li><li>Reelhub</li></ul></div>
    </div>
    <div class="about-panel">
      <h3>WE ARE A CONSTRUCTION GROUP</h3>
      <p>Contrary to popular belief, Lorem Ipsum is not simply random text. It has roots in a piece of classical Latin literature from 45 BC, making it over 2000 years old. Aldo Renwick, a Latin professor at Marlow-Kent</p>
      <p>Contrary to popular belief, Lorem Ipsum is not simply random text. It has roots in a piece of classical Latin literature from 45 BC, making <a class="read-more">Read More</a></p>
    </div>
  </section>

  <footer class="site-footer">
    <div class="copyright">© 2016 Halvery Building , all rights reserved</div>
    <nav class="footer-nav"><span>Home</span><span>About</span><span>Bio</span><span>Projects</span><span>Contact us</span></nav>
  </footer>
</body>
</html>
```